Painting Contractor Business Card Design

We are looking for a cool, bold, modern, polished, business card design. We are a high-end residential painting contractor. Please incorporate our logo and keep with our green/black color scheme. We are interested in seeing 2-sided and 1-sided options. Thank you very much!

Industry/Entity Type

Business

Contact Information for Business Card

Info for the card:
Owen Talsky
mobile 206-555-0193
email owen@kestrowfinish.net
web www.kestrowfinish.net

```html
<!DOCTYPE html>
<html lang="en">
<head>
<meta charset="utf-8">
<title>Kestrow Finish – Business Card</title>
<link href="https://fonts.googleapis.com/css2?family=Montserrat:wght@600&family=Saira+Semi+Condensed:wght@400;500;600&display=swap" rel="stylesheet">
<style>
  :root {
    --backdrop: #161616;
    --green: #38a030;
    --green-deep: #2f8a28;
    --ink: #141414;
    --paper-light: #fafafa;
    --paper-mid: #dcdcdc;
    --rule: #2a2a2a;
  }
  * { box-sizing: border-box; margin: 0; padding: 0; }
  html, body { width: 1189px; height: 1200px; overflow: hidden; }
  body { background: var(--backdrop); position: relative; font-family: "Saira Semi Condensed", sans-serif; }

  .card {
    position: absolute; left: 140px; width: 917px; height: 523px;
    background: radial-gradient(ellipse at 55% 55%, var(--paper-light) 0%, #ececec 45%, var(--paper-mid) 100%);
    overflow: hidden;
  }
  .card--front { top: 45px; }
  .card--back { top: 623px; }

  .band { position: absolute; left: 0; right: 0; background: linear-gradient(90deg, var(--green-deep), var(--green) 50%, var(--green-deep)); }
  .rule { position: absolute; left: 0; right: 0; height: 3px; background: var(--ink); }

  .wordmark { position: absolute; display: flex; align-items: center; gap: 26px; }
  .wordmark__mark { width: 84px; height: 98px; background: var(--ink); }
  .wordmark__name {
    font-family: "Montserrat", sans-serif; font-weight: 600; font-size: 58px;
    letter-spacing: 1px; color: var(--ink); line-height: 1; white-space: nowrap;
  }

  .card--front .band--top { top: 0; height: 176px; }
  .card--front .rule--top { top: 182px; }
  .card--front .rule--bottom { top: 481px; }
  .card--front .band--bottom { top: 487px; height: 36px; }
  .card--front .wordmark { left: 93px; top: 40px; }

  .person { position: absolute; left: 100px; top: 300px; width: 230px; text-align: center; }
  .person__name { font-weight: 600; font-size: 52px; line-height: 1; color: var(--ink); transform: translateY(-60px); }
  .person__role { font-weight: 500; font-size: 19px; color: var(--ink); transform: translateY(-58px); }

  .divider { position: absolute; left: 451px; top: 242px; width: 1.5px; height: 175px; background: var(--rule); }

  .contacts { position: absolute; left: 523px; top: 266px; width: 288px; list-style: none; border-top: 1px solid var(--rule); }
  .contacts__item {
    display: flex; align-items: center; gap: 19px; height: 43px;
    border-bottom: 1px solid var(--rule); font-size: 21px; color: var(--ink);
  }
  .contacts__icon { width: 24px; height: 22px; background: var(--green); flex: none; display: flex; align-items: center; justify-content: center; }
  .contacts__icon svg { width: 14px; height: 14px; }

  .card--back .band--top { top: 0; height: 45px; }
  .card--back .rule--top { top: 50px; }
  .card--back .rule--bottom { top: 470px; }
  .card--back .band--bottom { top: 479px; height: 44px; }
  .card--back .wordmark { left: 106px; top: 212px; }
</style>
</head>
<body>

<section class="card card--front">
  <div class="band band--top"></div>
  <div class="rule rule--top"></div>
  <div class="wordmark">
    <span class="wordmark__mark" aria-hidden="true"></span>
    <span class="wordmark__name">KESTROW FINISH</span>
  </div>

  <div class="person">
    <h1 class="person__name">Owen Talsky</h1>
    <p class="person__role">Managing Director</p>
  </div>

  <div class="divider"></div>

  <ul class="contacts">
    <li class="contacts__item">
      <span class="contacts__icon"><svg viewBox="0 0 16 16"><path d="M3 1.5l3 .5 1 3-1.8 1.3a8 8 0 0 0 4.5 4.5L11 9l3 1 .5 3-2 1.5C6.5 14 2 9.5 1.5 3.5z" fill="#141414"/></svg></span>
      206-555-0193
    </li>
    <li class="contacts__item">
      <span class="contacts__icon"><svg viewBox="0 0 16 16"><rect x="1" y="3" width="14" height="10" fill="#141414"/><path d="M1 3l7 6 7-6M1 13l5-5M15 13l-5-5" stroke="#38a030" stroke-width="1.2" fill="none"/></svg></span>
      owen@kestrowfinish.net
    </li>
    <li class="contacts__item">
      <span class="contacts__icon"><svg viewBox="0 0 16 16"><circle cx="8" cy="8" r="6.5" fill="#141414"/><path d="M5 4c2 1 1 3 3 3s1 3-1 4M10 3c0 2 2 2 3 3" stroke="#38a030" stroke-width="1.4" fill="none"/></svg></span>
      www.kestrowfinish.net
    </li>
  </ul>

  <div class="rule rule--bottom"></div>
  <div class="band band--bottom"></div>
</section>

<section class="card card--back">
  <div class="band band--top"></div>
  <div class="rule rule--top"></div>
  <div class="wordmark">
    <span class="wordmark__mark" aria-hidden="true"></span>
    <span class="wordmark__name">KESTROW FINISH</span>
  </div>
  <div class="rule rule--bottom"></div>
  <div class="band band--bottom"></div>
</section>

</body>
</html>
```